Rick Halvorsen's Personal Guitar Bench - a multi-use workstation for you and your guitar

A guitar workstation/stand. A furniture grade device that serves as a workstation to repair, restring, refurbish, clean, maintain, and ultimately display your guitar. The guitar can be held held securely and safely lying on it back, it's face, either side, and comes with a stand for it to slide in when work is complete to display or Store.

Target Market(s)

Electric, acoustic, and most other guitar owners. Luthiers. Guitar techs.

Industry/Entity Type

Music Training

Requirements
Must have
• Needs to explain what the Workshop does, hit on the aesthetics, size, founder/inventor etc. I forwarded much verbiage that has been used from other sources with my pictures. Our website is rickhalvorsen.com which should be somewhere on the Brochure as well. Maybe bullet points. - for use with acoustic, electric, and most guitars - holds guitar face up, face down, either side, and a vertical display with stand. - made with non-reactive materials at guitar touch points - use for repairing refurbishing, cleaning, restringing, constructing, and maintaining - Any more you can think of. We are not 100% sure of the materials we are using yet so instead of being specific say something like made with only the highest grade materials, furniture-grade quality
Nice to have
• We are down-to-earth people wanting to show people a high-quality product. We are taking these brochures to BRETT January2018. There will be over 100,000 music people/celebrities/buyers there. So we have one shot. Hoping you can help us with an awesome brochure. The colors on our website would be nice Rickhalvorsen.com
Should not have
• Cute

```html
<!DOCTYPE html>
<html lang="en">
<head>
<meta charset="utf-8">
<title>Rick Halvorsen's Personal Guitar Bench – Trifold</title>
<link href="https://fonts.googleapis.com/css2?family=Lobster&family=Exo+2:wght@600;700&family=Lato:wght@400;700&display=swap" rel="stylesheet">
<style>
  :root {
    --stage: #dcdcdc;
    --wood-dark: #4a2614;
    --wood-mid: #7a4326;
    --wood-light: #98582f;
    --band: #3f2a28;
    --band-edge: #6b4a45;
    --gold: #e7b777;
    --gold-deep: #c98a45;
    --cream: #f4efe6;
    --ink: #2b1a12;
    --veil: rgba(240, 214, 190, 0.8);
    --veil-line: #c99a63;
    --guitar-top: #d98a3a;
    --guitar-edge: #8d4a1e;
  }
  * { box-sizing: border-box; margin: 0; padding: 0; }
  html, body { width: 1200px; height: 1200px; overflow: hidden; }
  body {
    background: var(--stage);
    font-family: "Lato", sans-serif;
    display: flex; align-items: center; justify-content: center;
  }
  .trifold {
    width: 1120px; height: 880px;
    display: grid; grid-template-columns: repeat(3, 1fr);
    box-shadow: 0 14px 30px rgba(0,0,0,.3);
  }
  .panel { position: relative; overflow: hidden; }
  .panel + .panel { border-left: 1px solid rgba(0,0,0,.25); }
  .wood {
    position: absolute; inset: 0;
    background: linear-gradient(100deg, var(--wood-dark) 0%, var(--wood-light) 38%, var(--wood-mid) 65%, var(--wood-dark) 100%);
  }
  .photo { position: absolute; }

  /* left panel */
  .photo--founder {
    left: 0; top: 0; width: 100%; height: 440px;
    background: linear-gradient(180deg, #8a6c5a 0%, #7d6c66 50%, rgba(122,67,38,0) 100%);
  }
  .about-founder { position: absolute; left: 26px; right: 26px; top: 452px; color: var(--cream); }
  .about-founder h2 { font-family: "Exo 2", sans-serif; font-weight: 600; font-size: 25px; letter-spacing: .5px; }
  .script-name { font-family: "Lobster", cursive; color: var(--gold); font-size: 20px; border-bottom: 1px solid rgba(244,239,230,.5); padding-bottom: 4px; margin-bottom: 10px; }
  .about-founder p { font-size: 11.6px; line-height: 1.32; text-align: justify; margin-bottom: 12px; }
  .photo--guitar-bench {
    left: 0; bottom: 0; width: 100%; height: 175px;
    background: linear-gradient(0deg, #6a3a1f 0%, #c9a06f 55%, rgba(156,90,51,0) 100%);
  }

  /* middle panel */
  .veil {
    position: absolute; left: 14px; right: 14px; top: 20px; bottom: 20px;
    background: var(--veil); border: 2px solid var(--veil-line);
    outline: 1px solid rgba(201,154,99,.6); outline-offset: -8px;
    padding: 48px 30px 0; text-align: center; color: var(--ink);
  }
  .eyebrow { font-family: "Exo 2", sans-serif; font-weight: 600; font-size: 26px; color: var(--gold-deep); line-height: 1; }
  .veil h3 { font-family: "Exo 2", sans-serif; font-weight: 600; font-size: 27px; margin-bottom: 18px; }
  .veil p { font-size: 11.6px; line-height: 1.3; text-align: justify; text-align-last: center; }
  .wordmark { font-family: "Lato", sans-serif; font-weight: 700; color: var(--ink); }
  .veil .wordmark--sign { margin-top: 96px; font-size: 20px; }
  .tagline { font-size: 6px; letter-spacing: 1.5px; margin-top: 2px; }
  .partner { margin-top: 42px; font-size: 24px; letter-spacing: 1px; }
  .follow { margin-top: 18px; font-family: "Exo 2", sans-serif; font-weight: 600; font-size: 21px; }
  .social { display: flex; gap: 6px; justify-content: center; margin-top: 8px; }
  .social span { background: var(--ink); color: var(--cream); font-size: 9px; padding: 4px 5px; }

  /* cover panel */
  .brand-band {
    position: absolute; left: 0; right: 0; top: 70px; height: 82px;
    background: var(--band); border-top: 2px solid var(--band-edge); border-bottom: 2px solid var(--band-edge);
    display: flex; flex-direction: column; align-items: center; justify-content: center; color: var(--cream);
  }
  .brand-band .wordmark { color: var(--cream); font-size: 26px; }
  .cover-title { position: absolute; right: 28px; top: 186px; text-align: right; }
  .cover-title .name { font-family: "Lobster", cursive; color: var(--gold); font-size: 38px; }
  .cover-title .product { font-family: "Exo 2", sans-serif; font-weight: 700; color: var(--cream); font-size: 27px; line-height: 1.3; }
  .photo--cover-guitar {
    left: 48px; top: 330px; width: 250px; height: 470px; border-radius: 6px;
    background: linear-gradient(160deg, #5a3320 0%, var(--guitar-edge) 30%, var(--guitar-top) 70%, #a8561f 100%);
    box-shadow: 0 10px 24px rgba(0,0,0,.35);
  }
  .site { position: absolute; bottom: 22px; left: 0; right: 0; text-align: center; color: var(--cream); font-size: 13px; letter-spacing: 3px; }
</style>
</head>
<body>
<main class="trifold">
  <section class="panel panel--founder">
    <div class="wood" role="img" aria-label="Rosewood texture background"></div>
    <div class="photo photo--founder" role="img" aria-label="Photo of Rick Halvorsen working beside the guitar bench"></div>
    <div class="about-founder">
      <h2>ABOUT</h2>
      <div class="script-name">Rick Halvorsen</div>
      <p>You will likely find Rick working in his wood shop in a small town in northern Idaho. He will be exploring ways to bring to life what he envisioned at last night's campfire. He will be inspired by the sights and sounds of nature. In his mind's eye his vision will be something useful, something beautiful, and likely something you've never seen before.</p>
      <p>Rick loves music, all kinds. He loves guitars. Put together these passions with Rick's integrity and tenacious personality and you can bet there will come to life a product you would be happy to own and proud to give.</p>
    </div>
    <div class="photo photo--guitar-bench" role="img" aria-label="Photo of an acoustic guitar resting on the bench"></div>
  </section>

  <section class="panel panel--workshop">
    <div class="wood" role="img" aria-label="Rosewood texture background"></div>
    <div class="veil">
      <div class="eyebrow">ABOUT</div>
      <h3>Our Workshop</h3>
      <p>The functionality was the most important aspect of this product. We thought there has to be a better way than putting a towel on the kitchen table to change the strings, holding it on our lap or between our legs for cleaning, or creating a makeshift neck hold out of pillows for repairs. The PGB was designed to hold the guitar safely and securely in 3 positions, face-up, back-up, and on its side. Basically, a one-stop workshop! But there's more... After months and months of creating, and prototype after prototype, we thought we basically had it nailed. But we wanted to be sure. Quality is everything to us! We searched and found the 5 best engineers for the job. The PGB went from awesome to phenomenal! The look, feel, and function had now been perfected. And it got something new! A stand! The engineers designed a unique, collapsible stand for the PGB. With a guitar held tight (no matter what position), the PGB will easily slide into the stand for vertically displaying or holding your guitar. Nice, don't you think?!</p>
      <div class="wordmark wordmark--sign">Rick Halvorsen</div>
      <div class="tagline">PERSONAL GUITAR BENCH</div>
      <div class="wordmark partner">BRETT</div>
      <div class="follow">FOLLOW US ON</div>
      <div class="social"><span>Pagebook</span><span>Chirper</span><span>Vidreel</span><span>Pinwall</span></div>
    </div>
  </section>

  <section class="panel panel--cover">
    <div class="wood" role="img" aria-label="Rosewood texture background"></div>
    <div class="brand-band">
      <div class="wordmark">Rick Halvorsen</div>
      <div class="tagline">PERSONAL GUITAR BENCH</div>
    </div>
    <div class="cover-title">
      <div class="name">Rick Halvorsen</div>
      <div class="product">Personal Guitar<br>Bench</div>
    </div>
    <div class="photo photo--cover-guitar" role="img" aria-label="Photo of a classical guitar held upright in the bench stand"></div>
    <div class="site">www.rickhalvorsen.com</div>
  </section>
</main>
</body>
</html>
```